domestic violence campaign

To Whom It May Concern:

We are fully aware that domestic violence can enter anyone’s life at any given time. As women we are faced with many demands as mothers, daughters, wives, sisters, providers, and friends. We often lose ourselves and our confidence. Bright Maple Circle (BMC) Transitional Center of Western New York has embarked on a whole new way of intervention and prevention. As a domestic violence survivor I have created a facility and ideals which will enforce a revolution of Domestic Violence victims. For many years, growing up in suburbs of Western New York, I have come to terms with this fight. Domestic Violence can be stopped and prevented. As a domestic violence victim myself, being in live-in facility, as well as six different domestic violence shelters throughout the state, I fled from my domestic violence abuse. Without those temporary facilities, all that comes to my mind is death. They helped me rebuild and save my life but something was missing – zero education, training programs, parenting classes, personal strengthening workshops, on site at all. Considering the limited amount of time (30-45 days in an average shelter) and lack of resources, I was in need of the tools needed to move me from being a victim to having a stable life.
Opening more doors in Western New York is essential with the surrounding agencies and shelters overwhelmed from assisting women of crisis. Many issues have risen, as a result, such as: over-crowding, long waiting lists, and zero educational training with an on-site teaching curriculum. A repeated vicious cycle – victims regressing and not progressing with over 4000 cases of domestic violence reported throughout Erie County. The opening Bright Maple Circle (BMC) Transitional Center of Western New York will provide a 9-24 month live-in facility, along with educational and training programs on-site that will serve as important tools to domestic violence victims. These educational based facilities and services are well needed for Western New York. Our trained certified staff will provide endless help to domestic violence victim. They will feel safe as they rebuild their lives and take advantage of our educational curriculum that has been designed to increase awareness and provide steppingstones to move the victims into confident stable independent human beings. Our clients will receive complete educational training, state testing, parenting classes, as well as strengthening, coping, and developing skills here at our facility. Bright Maple Circle (BMC) Transitional Center is asking for your support.
Sincerely,
Rosalind Pemberton
President and CEO/website bmctcq.org
Bright Maple Circle (BMC) Transitional Center of WNY

Industry/Entity Type

Training

Requirements
Nice to have
• we have already created our T-shirt/we will like for our T-shirt to be the center of the campaign to T-shirt reads
V IOLENCE
O N
W OMEN
S TOPS the campaign is to raise money so we can open doors and save lives

```html
<!DOCTYPE html>
<html lang="en">
<head>
<meta charset="utf-8">
<title>BMC Domestic Violence Campaign Card</title>
<link rel="stylesheet" href="https://fonts.googleapis.com/css2?family=PT+Sans+Narrow&family=Special+Elite&display=swap">
<style>
  :root {
    --page-bg: #e4e4e4;
    --card-edge: #ffffff;
    --maroon-deep: #3b0003;
    --maroon-mid: #5a0a10;
    --crimson-glow: #a11c27;
    --photo-light: #9a9a9a;
    --photo-dark: #1e1e1e;
    --type-white: #ffffff;
  }
  html, body {
    margin: 0;
    width: 1200px;
    height: 1000px;
    overflow: hidden;
    background: var(--page-bg);
  }
  .campaign-card {
    position: absolute;
    left: 100px;
    top: 62px;
    width: 1000px;
    height: 875px;
    display: block;
  }
  .card-type {
    font-family: "PT Sans Narrow", "Arial Narrow", sans-serif;
    fill: var(--type-white);
  }
  .slogan {
    font-family: "Special Elite", "Courier New", monospace;
    fill: var(--type-white);
  }
  .cross-line {
    fill: none;
    stroke: var(--type-white);
    stroke-width: 4;
  }
</style>
</head>
<body>
<svg class="campaign-card" viewBox="0 0 656 574" xmlns="http://www.w3.org/2000/svg">
  <defs>
    <radialGradient id="crimsonGlow" cx="130" cy="150" r="260" gradientUnits="userSpaceOnUse">
      <stop offset="0" stop-color="var(--crimson-glow)"/>
      <stop offset="0.55" stop-color="var(--maroon-mid)"/>
      <stop offset="1" stop-color="var(--maroon-deep)"/>
    </radialGradient>
    <linearGradient id="portraitTone" x1="0" y1="0" x2="1" y2="1">
      <stop offset="0" stop-color="var(--photo-light)"/>
      <stop offset="0.6" stop-color="#4a4a4a"/>
      <stop offset="1" stop-color="var(--photo-dark)"/>
    </linearGradient>
    <linearGradient id="portraitFade" x1="0" y1="0" x2="0" y2="1">
      <stop offset="0.8" stop-color="var(--maroon-deep)" stop-opacity="0"/>
      <stop offset="1" stop-color="var(--maroon-deep)" stop-opacity="1"/>
    </linearGradient>
  </defs>

  <!-- card base -->
  <rect class="card-base" x="0" y="0" width="656" height="574" fill="var(--card-edge)"/>
  <rect class="card-field" x="4" y="4" width="648" height="566" fill="var(--maroon-deep)"/>

  <!-- upper glow panel -->
  <rect class="upper-panel" x="4" y="4" width="364" height="306" fill="url(#crimsonGlow)"/>

  <!-- portrait area -->
  <g class="portrait" role="img" aria-label="Black and white close-up photograph of a woman's face showing one eye">
    <rect x="368" y="4" width="240" height="306" fill="url(#portraitTone)"/>
    <rect x="368" y="4" width="240" height="306" fill="url(#portraitFade)"/>
  </g>

  <!-- right-hand panels around the cross arm -->
  <path class="corner-panel" d="M475 4 H652 V90 H495 Q475 90 475 70 Z" fill="var(--maroon-deep)"/>
  <path class="corner-panel" d="M605 90 H652 V215 H605 Z" fill="var(--maroon-deep)"/>
  <path class="corner-panel" d="M480 310 V235 Q480 215 500 215 H652 V310 Z" fill="var(--maroon-deep)"/>

  <!-- cross outlines -->
  <path class="cross-line" d="M4 65 H72 Q90 65 90 47 V4"/>
  <path class="cross-line" d="M240 4 V50 Q240 70 260 70 H368"/>
  <path class="cross-line" d="M4 255 H72 Q90 255 90 273 V310"/>
  <path class="cross-line" d="M475 4 V70 Q475 90 495 90 H587 Q605 90 605 108 V197 Q605 215 587 215 H500 Q480 215 480 235 V310"/>

  <!-- organisation name -->
  <g class="card-type org-name" font-size="20" text-anchor="middle">
    <text x="162" y="34">Bright Maple Circle</text>
    <text x="162" y="64">Transitional</text>
    <text x="162" y="94">Center of</text>
    <text x="162" y="124">Western New York</text>
  </g>

  <!-- donate call -->
  <g class="card-type donate" font-size="20">
    <text x="530" y="40">Donate Today</text>
    <text x="530" y="70">bmctcq.org</text>
  </g>

  <!-- headline -->
  <text class="card-type headline" x="52" y="236" font-size="48">Domestic Violence</text>

  <!-- message -->
  <g class="card-type message" font-size="24" text-anchor="middle">
    <text x="328" y="355">Can enter anyone’s life at any given time</text>
    <text x="328" y="408">Domestic Violence can be stopped or prevented</text>
    <text x="328" y="458">Place your Ad, and speak out take the</text>
    <text x="328" y="490">Vows with BMC</text>
  </g>

  <!-- slogan -->
  <text class="slogan" x="328" y="557" font-size="40" text-anchor="middle" textLength="592" lengthAdjust="spacingAndGlyphs">VIOLENCE ON WOMEN STOPS NOW</text>
</svg>
</body>
</html>
```